Rebrand existing website with new identity and colours as supplied

I have an old website that I would like updating with a new identity.
The website is at www.larchvalefunding.com
The new branding and changes are as set out below.

Target Market(s)

Buyers and sellers of SME businesses

Industry/Entity Type

Financial services

Coding

Coded - Design and coding required

Number of Pages Required

4 page

Requirements
Must have
• In addition to the small number of new pages I would like to retain the existing structure and pages - simply rebranded

```html
<!DOCTYPE html>
<html lang="en">
<head>
<meta charset="utf-8">
<title>Larchvale Advisory – Business Acquisition Finance</title>
<link href="https://fonts.googleapis.com/css2?family=Roboto:wght@400;500;700;900&family=Poppins:wght@400;500;600&display=swap" rel="stylesheet">
<style>
:root{
  --navy:#141c4f;
  --navy-deep:#0f1640;
  --red:#e3061b;
  --ink:#1d1d1f;
  --muted:#555a66;
  --line:#c9ccd6;
  --paper:#ffffff;
  --mist:#eef0f4;
}
*{box-sizing:border-box;margin:0;padding:0}
html,body{width:1200px;height:3814px;overflow:hidden}
body{position:relative;background:var(--paper);font-family:"Poppins",sans-serif;color:var(--ink)}
.abs{position:absolute}
h1,h2,h3,h4{font-family:"Roboto",sans-serif;font-weight:700}

/* header */
.site-header{left:0;top:0;width:1200px;height:85px;background:var(--navy);z-index:5}
.brand{left:92px;top:22px;width:160px;display:flex;align-items:center;gap:9px;color:#fff;font-family:"Roboto",sans-serif;font-weight:500;font-size:15px;line-height:18px}
.brand-mark{flex:0 0 auto;width:34px;height:34px;border:2px solid #fff}
.main-nav{left:271px;top:36px;display:flex;gap:28px}
.main-nav a{color:#fff;font-family:"Roboto",sans-serif;font-weight:700;font-size:11.5px;text-decoration:none;letter-spacing:.2px;white-space:nowrap}
.btn{display:flex;align-items:center;justify-content:center;background:var(--red);color:#fff;border-radius:30px;font-family:"Roboto",sans-serif;font-weight:700;text-decoration:none}
.header-cta{left:943px;top:20px;width:119px;height:50px;font-size:15px}

/* hero */
.hero-photo{left:0;top:85px;width:1200px;height:620px;background:linear-gradient(135deg,#2a3450 0%,#4a5a78 35%,#8e93a0 60%,#5b4a44 100%)}
.hero-panel{left:193px;top:241px;width:780px;height:277px;background:rgba(40,44,58,.55);text-align:center;color:#fff}
.hero-panel h1{margin-top:15px;font-size:55px;line-height:56px;font-weight:900;letter-spacing:.3px}
.hero-panel p{margin:14px auto 0;width:680px;font-size:13px;line-height:27px}
.hero-cta{left:504px;top:444px;width:160px;height:52px;font-size:15px}
.dots{left:565px;top:596px;display:flex;gap:7px}
.dots span{width:13px;height:13px;border:1.5px solid #fff;border-radius:50%}
.dots span:first-child{background:#fff}

.section-title{width:1200px;left:0;text-align:center;font-size:31px;color:var(--ink)}
.section-title::after{content:"";display:block;width:62px;height:3px;background:var(--red);margin:13px auto 0}
.section-title.light{color:#fff}
.section-title.light::after{display:none}

/* services */
.arrow{width:28px;height:48px}
.service-card{width:227px;height:333px;background:#fff;box-shadow:0 2px 12px rgba(0,0,0,.1);border-radius:4px;text-align:center;padding:8px 0 0}
.service-card h3{font-size:20px;height:32px;color:var(--navy)}
.service-card .photo{height:159px;background:linear-gradient(135deg,#6e7688,#c8c1b4)}
.service-card p{font-size:12px;line-height:25px;color:var(--ink);padding:12px 8px 0}
.service-card.active{background:var(--red)}
.service-card.active h3,.service-card.active p{color:#fff}

/* about */
.about-band{left:0;top:1271px;width:1200px;height:518px;background:linear-gradient(120deg,#1b2456,#141c4f 60%,#1e2a5c)}
.about-text{left:140px;top:1401px;width:920px;text-align:center;color:#fff;font-size:13px;line-height:26px}
.video-frame{left:150px;top:1574px;width:900px;height:403px;border:4px solid #fff;box-shadow:0 4px 14px rgba(0,0,0,.25);background:linear-gradient(135deg,#2c3853,#6a7184 50%,#8a6b5c)}
.play{left:528px;top:1717px;width:144px;height:120px}

/* blog */
.blog-card{width:303px;height:412px;background:#fff;text-align:center}
.blog-card.raised{box-shadow:0 3px 14px rgba(0,0,0,.14)}
.blog-card .photo{height:194px;background:linear-gradient(135deg,#8b8f97,#d1cdc5)}
.blog-card h4{font-size:15px;line-height:28px;padding:14px 8px 0;color:var(--ink);font-weight:500}
.blog-card p{font-size:12.5px;line-height:28px;color:var(--muted);padding:4px 10px 0}
.author{display:flex;align-items:center;justify-content:center;gap:6px;margin-top:10px;font-family:"Roboto",sans-serif;font-weight:700;font-size:11px;color:#444}
.author i{width:18px;height:18px;background:var(--red)}
.view-all{left:508px;top:2596px;width:184px;height:51px;font-size:15px}

/* contact */
.contact-band{left:0;top:2720px;width:1200px;height:720px;background:linear-gradient(180deg,#f4f5f8,#e6e8ee)}
.contact-title::after{background:var(--navy)}
.mail-art{left:281px;top:2940px;width:282px;height:281px;border-radius:16px;background:linear-gradient(135deg,rgba(227,6,27,.18),rgba(20,28,79,.2))}
.field{left:637px;width:318px;height:38px;border:1px solid var(--line);border-radius:20px;background:#fff;font-size:11px;color:#333;padding:11px 0 0 21px}
.field.message{height:82px;border-radius:12px}
.send{left:637px;top:3206px;width:318px;height:39px;font-size:15px}

/* footer */
.footer-band{left:0;top:3300px;width:1200px;height:514px}
.footer-brand{left:196px;top:3508px;display:flex;align-items:center;gap:10px;color:#fff;font-family:"Roboto",sans-serif;font-weight:500;font-size:29px}
.footer-brand .brand-mark{width:42px;height:42px}
.footer-about{left:176px;top:3547px;width:244px;color:#fff;font-size:12px;line-height:27px;text-align:center}
.footer-col h4{color:#fff;font-size:14.5px;font-weight:500;margin-bottom:14px}
.footer-col li{list-style:none;color:#fff;font-size:12px;line-height:27.3px}
.footer-col li::before{content:"»";margin-right:16px}
.socials{display:flex;gap:15px}
.socials span{width:36px;height:36px;border-radius:50%;background:#fff;border:3px solid var(--red)}
.rule{left:125px;top:3740px;width:950px;height:1px;background:rgba(255,255,255,.2)}
.copyright{left:0;top:3754px;width:1200px;text-align:center;color:#fff;font-size:12px}
.copyright em{font-style:normal;color:var(--red)}
</style>
</head>
<body>

<header class="site-header abs">
  <div class="brand abs"><span class="brand-mark"></span><span>Larchvale<br>Advisory Ltd</span></div>
  <nav class="main-nav abs">
    <a href="#">HOME</a><a href="#">ABOUT</a><a href="#">WORKING CAPITAL FINANCE</a><a href="#">ASSET FINANCE</a><a href="#">PROPERTY FINANCE</a><a href="#">CONTACT</a>
  </nav>
  <a class="btn header-cta abs" href="#">GET IN TOUCH</a>
</header>

<div class="hero-photo abs" role="img" aria-label="Business people reviewing financial charts and signing documents at a desk"></div>
<svg class="abs" style="left:0;top:560px" width="1200" height="200" viewBox="0 560 1200 200">
  <polygon fill="#fff" points="0,585 39,597 145,604 274,632 379,618 465,647 687,700 789,652 994,616 1097,632 1200,600 1200,760 0,760"/>
  <polyline fill="none" stroke="#e3061b" stroke-width="2" points="0,585 39,597 145,604 274,632 379,618 465,647 687,700 789,652 994,616 1097,632 1200,600"/>
  <g fill="#e3061b">
    <circle cx="39" cy="597" r="6"/><circle cx="145" cy="604" r="6"/><circle cx="274" cy="632" r="6"/><circle cx="465" cy="647" r="6"/><circle cx="789" cy="652" r="6"/><circle cx="1097" cy="632" r="6"/>
    <circle cx="379" cy="618" r="14" opacity=".85"/><circle cx="687" cy="700" r="14" opacity=".85"/><circle cx="994" cy="616" r="14" opacity=".85"/>
  </g>
</svg>
<div class="hero-panel abs">
  <h1>ALL THE HELP YOU NEED<br>TO BUY A BUSINESS</h1>
  <p>Lorem ipsum dolor sit amet, consectetur adipiscing elit, sed do eiusmod tempor incididunt ut labore et dolore magna aliqua. Quis ipsum suspendisse ultrices gravida.</p>
</div>
<a class="btn hero-cta abs" href="#">GET STARTED</a>
<div class="dots abs"><span></span><span></span><span></span><span></span></div>

<h2 class="section-title abs" style="top:774px">OUR SERIVCES</h2>
<svg class="arrow abs" style="left:55px;top:1000px" viewBox="0 0 28 48"><polyline points="24,4 4,24 24,44" fill="none" stroke="#111" stroke-width="2.5"/></svg>
<svg class="arrow abs" style="left:1118px;top:1000px" viewBox="0 0 28 48"><polyline points="4,4 24,24 4,44" fill="none" stroke="#111" stroke-width="2.5"/></svg>

<article class="service-card abs" style="left:117px;top:859px"><h3>BUSINESS LOANS</h3><div class="photo" role="img" aria-label="Colleagues discussing a loan at a laptop"></div><p>Lorem ipsum dolor sit amet, consec-tetur adipiscing elit, sed do eiusmod tempor incididunt ut labore et dolore magna.</p></article>
<article class="service-card active abs" style="left:363px;top:859px"><h3>ASSET FINANCE</h3><div class="photo" role="img" aria-label="Hands holding a money bag"></div><p>Lorem ipsum dolor sit amet, consec-tetur adipiscing elit, sed do eiusmod tempor incididunt ut labore et dolore magna.</p></article>
<article class="service-card abs" style="left:610px;top:859px"><h3>TRADE FINANCE</h3><div class="photo" role="img" aria-label="Presenter in an office beside a chart board"></div><p>Lorem ipsum dolor sit amet, consec-tetur adipiscing elit, sed do eiusmod tempor incididunt ut labore et dolore magna.</p></article>
<article class="service-card abs" style="left:856px;top:859px"><h3>INVOICE FINANCE</h3><div class="photo" role="img" aria-label="Person reviewing invoices at a laptop"></div><p>Lorem ipsum dolor sit amet, consec-tetur adipiscing elit, sed do eiusmod tempor incididunt ut labore et dolore magna.</p></article>

<section class="about-band abs" role="img" aria-label="Dark blue business backdrop"></section>
<h2 class="section-title light abs" style="top:1328px">ABOUT LARCHVALE ADVISORY</h2>
<p class="about-text abs">The Larchvale Advisory team have many years' experience as entrepreneurs, private equity investors, and senior lenders. We've bought, sold, founded, and funded many businesses over the last 40 years.We have developed the tools to identify the optimal structure for your deal, and we have the contacts to help you get it funded and completed.</p>
<div class="video-frame abs" role="img" aria-label="Video still of a team reviewing financial reports"></div>
<svg class="play abs" viewBox="0 0 144 120"><ellipse cx="72" cy="60" rx="72" ry="60" fill="rgba(60,60,70,.55)"/><circle cx="72" cy="60" r="34" fill="#2a2a33"/><polygon points="64,44 64,76 88,60" fill="#fff"/></svg>

<h2 class="section-title abs" style="top:2048px">OUR LATEST BLOG</h2>
<article class="blog-card abs" style="left:130px;top:2125px"><div class="photo" role="img" aria-label="Hands typing on a laptop beside a calculator"></div><h4>LOREM IPSUM DOLOR SIT AMET CON SECTETUR ADIPISCING ELIT.</h4><p>Lorem ipsum dolor sit amet, consectetur adipiscing elit, sed do eiusmod tempor incidi-dunt ut labore et dolore magna aliqua.</p><div class="author"><i></i>Brightwell</div></article>
<article class="blog-card raised abs" style="left:449px;top:2125px"><div class="photo" role="img" aria-label="Presenter in a modern office"></div><h4>LOREM IPSUM DOLOR SIT AMET CON SECTETUR ADIPISCING ELIT.</h4><p>Lorem ipsum dolor sit amet, consectetur adipiscing elit, sed do eiusmod tempor incidi-dunt ut labore et dolore magna aliqua.</p><div class="author"><i></i>Brightwell</div></article>
<article class="blog-card abs" style="left:766px;top:2125px"><div class="photo" role="img" aria-label="Business handshake over a desk"></div><h4>LOREM IPSUM DOLOR SIT AMET CON SECTETUR ADIPISCING ELIT.</h4><p>Lorem ipsum dolor sit amet, consectetur adipiscing elit, sed do eiusmod tempor incidi-dunt ut labore et dolore magna aliqua.</p><div class="author"><i></i>Brightwell</div></article>
<a class="btn view-all abs" href="#">VIEW ALL BLOG</a>

<section class="contact-band abs"></section>
<h2 class="section-title contact-title abs" style="top:2820px">GET IN TOUCH</h2>
<div class="mail-art abs" role="img" aria-label="Illustration of an envelope with a checked message"></div>
<div class="field abs" style="top:2918px">First Name</div>
<div class="field abs" style="top:2966px">Last Name</div>
<div class="field abs" style="top:3015px">Phone</div>
<div class="field abs" style="top:3064px">Email Address</div>
<div class="field message abs" style="top:3110px">Message</div>
<a class="btn send abs" href="#">SEND</a>

<svg class="footer-band abs" viewBox="0 3300 1200 514" width="1200" height="514">
  <polygon fill="#141c4f" points="0,3406 102,3389 207,3404 293,3374 410,3365 512,3322 622,3350 736,3377 820,3404 918,3389 1097,3396 1177,3426 1200,3436 1200,3814 0,3814"/>
  <polyline fill="none" stroke="#e3061b" stroke-width="2" points="0,3406 102,3389 207,3404 293,3374 410,3365 512,3322 622,3350 736,3377 820,3404 918,3389 1097,3396 1177,3426 1200,3436"/>
  <g fill="#e3061b">
    <circle cx="102" cy="3389" r="6"/><circle cx="293" cy="3374" r="6"/><circle cx="410" cy="3365" r="6"/><circle cx="736" cy="3377" r="6"/><circle cx="918" cy="3389" r="6"/><circle cx="1177" cy="3426" r="6"/>
    <circle cx="207" cy="3404" r="14" opacity=".85"/><circle cx="512" cy="3322" r="14" opacity=".85"/><circle cx="820" cy="3404" r="14" opacity=".85"/>
  </g>
</svg>
<div class="footer-brand abs"><span class="brand-mark"></span>Larchvale</div>
<p class="footer-about abs">Lorem ipsum dolor sit amet, consectetur adipiscing elit.Lorem ipsum dolor sit amet, consectetur adipiscing elit.</p>
<div class="footer-col abs" style="left:466px;top:3480px"><h4>QUICK LINKS</h4><ul><li>Home</li><li>About</li><li>Working Capital Finance</li><li>Asset Finance</li><li>Property Finance</li><li>Contact</li></ul></div>
<div class="footer-col abs" style="left:687px;top:3480px"><h4>OUR SERVICES</h4><ul><li>Business Loans</li><li>Business Cash Advances</li><li>Revolving Credit Facilities</li><li>Tax bill and VAT funding</li><li>Trade Finance</li><li>Invoice Finance</li><li>Commercial Property Finance</li></ul></div>
<div class="footer-col abs" style="left:933px;top:3480px"><h4>FOLLOW US</h4><div class="socials"><span role="img" aria-label="Social profile"></span><span role="img" aria-label="Professional network profile"></span></div></div>
<div class="rule abs"></div>
<p class="copyright abs">© Copyrights 2022 <em>LARCHVALE ADVISORY</em> &nbsp; | &nbsp; All Rights Reserved</p>

</body>
</html>
```